Swimming pool service business postcard redesign

We need a fresh post card design for our pool service business based in San Diego called Tide Sweepers. We are a family based, local residential pool cleaning and maintenance company. we need an offer to stand out, our logo, our colors, etc on a 5.5x8 inch full color post card.

```html
<!DOCTYPE html>
<html lang="en">
<head>
<meta charset="utf-8">
<title>Tide Sweepers – Postcard Back</title>
<link rel="stylesheet" href="https://fonts.googleapis.com/css2?family=Oswald:wght@500;600;700&family=Poppins:wght@400;500;600&display=swap">
<style>
  :root {
    --brand-red: #e6401e;
    --brand-red-light: #ee5530;
    --brand-navy: #1d2f5c;
    --paper: #ffffff;
    --edge-grey: #ececec;
    --stamp-grey: #d6d6d6;
    --rule-grey: #b9b9b9;
    --ink: #222222;
  }
  * { margin: 0; padding: 0; box-sizing: border-box; }
  html, body { width: 1200px; height: 837px; overflow: hidden; background: var(--paper); }
  .postcard { position: relative; width: 1200px; height: 837px; background: var(--paper); overflow: hidden; }
  .panel-shape { position: absolute; inset: 0; }

  .headline {
    position: absolute; left: 60px; top: 58px;
    font-family: "Oswald", sans-serif; font-weight: 600;
    font-size: 46px; line-height: 1; color: var(--paper); letter-spacing: 0.5px;
    white-space: nowrap;
  }
  .headline-underline { position: absolute; left: 58px; top: 126px; }
  .intro {
    position: absolute; left: 60px; top: 156px; width: 620px;
    font-family: "Poppins", sans-serif; font-weight: 400;
    font-size: 31px; line-height: 44px; color: var(--paper);
  }

  .include-ribbon { position: absolute; left: 0; top: 314px; }
  .include-label {
    position: absolute; left: 60px; top: 318px;
    font-family: "Oswald", sans-serif; font-weight: 500;
    font-size: 36px; line-height: 50px; color: var(--paper);
  }
  .service-list { position: absolute; left: 60px; top: 390px; list-style: none; }
  .service-item { display: flex; align-items: center; height: 56px; margin-bottom: 24px; }
  .service-icon { width: 58px; height: 58px; flex: none; }
  .service-name {
    margin-left: 22px;
    font-family: "Poppins", sans-serif; font-weight: 500;
    font-size: 24px; color: var(--paper); white-space: nowrap;
  }

  .stamp-box { position: absolute; left: 954px; top: 56px; width: 180px; height: 180px; background: var(--stamp-grey); }

  .offer {
    position: absolute; left: 760px; top: 272px; width: 374px; height: 188px;
    border: 3px solid var(--brand-navy);
    text-align: center; padding-top: 14px;
  }
  .offer-kicker {
    font-family: "Oswald", sans-serif; font-weight: 500;
    font-size: 22px; letter-spacing: 2px; color: var(--brand-navy);
  }
  .offer-amount {
    font-family: "Oswald", sans-serif; font-weight: 700;
    font-size: 72px; line-height: 80px; color: var(--brand-red);
  }
  .offer-terms {
    font-family: "Poppins", sans-serif; font-weight: 500;
    font-size: 17px; color: var(--ink);
  }

  .address-to {
    position: absolute; left: 730px; top: 512px;
    font-family: "Poppins", sans-serif; font-size: 26px; color: var(--ink);
  }
  .address-line { position: absolute; height: 2px; background: var(--rule-grey); }

  .brand-mark {
    position: absolute; left: 830px; top: 728px;
    display: flex; align-items: center;
  }
  .brand-dot { width: 34px; height: 34px; border-radius: 50%; background: var(--brand-navy); flex: none; }
  .brand-name {
    margin-left: 14px;
    font-family: "Poppins", sans-serif; font-weight: 600;
    font-size: 32px; line-height: 1; color: var(--brand-navy); white-space: nowrap;
  }
</style>
</head>
<body>
<main class="postcard">
  <svg class="panel-shape" width="1200" height="837" viewBox="0 0 1200 837" aria-hidden="true">
    <polygon points="784,0 804,0 560,837 540,837" fill="var(--edge-grey)"/>
    <polygon points="0,0 784,0 540,837 0,837" fill="var(--brand-red)"/>
    <polygon points="560,0 784,0 540,837 420,837" fill="var(--brand-red-light)" opacity="0.45"/>
  </svg>

  <h1 class="headline">WHY CHOOSE TIDE SWEEPERS?</h1>
  <svg class="headline-underline" width="380" height="14" viewBox="0 0 380 14" aria-hidden="true">
    <path d="M2 8 C80 2 250 2 378 5 L372 11 C250 10 90 11 4 13 Z" fill="var(--brand-navy)"/>
  </svg>

  <p class="intro">We Help San Diego homeowners<br>enjoy a clean, healthy, worry-free pool<br>without the hassle.</p>

  <svg class="include-ribbon" width="430" height="58" viewBox="0 0 430 58" aria-hidden="true">
    <polygon points="0,0 430,0 404,29 430,58 0,58" fill="var(--brand-navy)"/>
  </svg>
  <h2 class="include-label">WHAT WE INCLUDE</h2>

  <ul class="service-list">
    <li class="service-item">
      <svg class="service-icon" viewBox="0 0 58 58" aria-hidden="true">
        <circle cx="29" cy="29" r="29" fill="var(--brand-navy)"/>
        <path d="M29 15 C24 23 20 28 20 33 a9 9 0 0 0 18 0 C38 28 34 23 29 15 Z" fill="none" stroke="#fff" stroke-width="2.4"/>
      </svg>
      <span class="service-name">Water Testing &amp; Chemical Balancing</span>
    </li>
    <li class="service-item">
      <svg class="service-icon" viewBox="0 0 58 58" aria-hidden="true">
        <circle cx="29" cy="29" r="29" fill="var(--brand-navy)"/>
        <rect x="19" y="15" width="20" height="27" rx="2" fill="none" stroke="#fff" stroke-width="2.2"/>
        <path d="M23 22h12M23 28h12M23 34h8" stroke="#fff" stroke-width="2"/>
      </svg>
      <span class="service-name">Professional Service Reports</span>
    </li>
    <li class="service-item">
      <svg class="service-icon" viewBox="0 0 58 58" aria-hidden="true">
        <circle cx="29" cy="29" r="29" fill="var(--brand-navy)"/>
        <path d="M14 36 q4 -4 8 0 t8 0 t8 0 t8 0" fill="none" stroke="#fff" stroke-width="2.2"/>
        <rect x="20" y="20" width="16" height="10" rx="2" fill="none" stroke="#fff" stroke-width="2.2"/>
        <path d="M36 24 L42 16" stroke="#fff" stroke-width="2.2"/>
      </svg>
      <span class="service-name">Weekly Pool Cleaning</span>
    </li>
    <li class="service-item">
      <svg class="service-icon" viewBox="0 0 58 58" aria-hidden="true">
        <circle cx="29" cy="29" r="29" fill="var(--brand-navy)"/>
        <rect x="21" y="15" width="16" height="28" rx="3" fill="none" stroke="#fff" stroke-width="2.2"/>
        <path d="M25 21h8M25 26h8M25 31h8M25 36h8" stroke="#fff" stroke-width="1.8"/>
      </svg>
      <span class="service-name">Basket &amp; Filter Cleaning</span>
    </li>
    <li class="service-item">
      <svg class="service-icon" viewBox="0 0 58 58" aria-hidden="true">
        <circle cx="29" cy="29" r="29" fill="var(--brand-navy)"/>
        <rect x="16" y="24" width="26" height="16" rx="2" fill="none" stroke="#fff" stroke-width="2.2"/>
        <circle cx="29" cy="32" r="4" fill="none" stroke="#fff" stroke-width="2"/>
        <path d="M22 24 v-6 h14 v6" fill="none" stroke="#fff" stroke-width="2.2"/>
      </svg>
      <span class="service-name">Equipment Monitoring</span>
    </li>
  </ul>

  <div class="stamp-box" aria-hidden="true"></div>

  <section class="offer" aria-label="Special offer">
    <p class="offer-kicker">NEW CUSTOMER OFFER</p>
    <p class="offer-amount">$50 OFF</p>
    <p class="offer-terms">your first month of weekly service</p>
  </section>

  <span class="address-to">To.</span>
  <div class="address-line" style="left:776px; top:537px; width:358px;"></div>
  <div class="address-line" style="left:656px; top:600px; width:478px;"></div>
  <div class="address-line" style="left:656px; top:666px; width:478px;"></div>

  <div class="brand-mark">
    <span class="brand-dot" aria-hidden="true"></span>
    <span class="brand-name">Tide Sweepers</span>
  </div>
</main>
</body>
</html>
```